Graphic Design Project adhesive label

We are a handkerchief wholesaler and require an adhesive sticker to stick on top left side single cello bag 170mm x 170mm. Then to run down the back of back noting our details. Flat and folded inside bag is a floral and or paisley ladies handkerchief.
Sticker approx 30cm wide 90mm long but folded at 45mm. 45mm down the front of bag and 45mm going down back of bag. Changed cm to mm.

Wording for Front sticker:

Marlowe Cloth
handkerchief
by .Tennick.

Back of sticker:

Made from imported English Marlowe cloth
100% cotton traditional hemstitch finish
www.tennick-example.com

Hi - Sorry made a mistake with measurements should be 170 mm not 170cm. Same with sticker mm's.                                     

Reason: Extending deadline as will be away until wednesday 2/5/13

Reason: Have been away and have not had a chance to consider designs, thanks for your patience. T

Target Market(s)

mature generally

Industry/Entity Type

Floral

Requirements
Must have
• prefer a lighter background
Nice to have
• Apart from wording some sort of back ground design, colour or symbol

```html
<!DOCTYPE html>
<html lang="en">
<head>
<meta charset="utf-8">
<title>Marlowe Cloth Handkerchief Labels by Tennick</title>
<link rel="stylesheet" href="https://fonts.googleapis.com/css2?family=Cormorant+Garamond:ital,wght@0,500;1,500&display=swap">
<style>
  :root {
    --canvas: #ffffff;
    --brown-deep: #3a2816;
    --brown-mid: #6b5236;
    --gold-light: #c9b98f;
    --paisley-cream: #e6e0c8;
    --paisley-sage: #b9b38f;
    --label-white: #ffffff;
    --ink: #241a10;
  }
  html, body {
    margin: 0;
    padding: 0;
    width: 1200px;
    height: 1147px;
    overflow: hidden;
    background: var(--canvas);
  }
  .canvas { display: block; width: 1200px; height: 1147px; }
  .script-text {
    font-family: "Cormorant Garamond", Georgia, serif;
    font-style: italic;
    font-weight: 500;
    fill: var(--ink);
  }
  .brand-name {
    font-family: "Cormorant Garamond", Georgia, serif;
    font-style: normal;
    font-weight: 500;
    fill: var(--ink);
    letter-spacing: 4px;
  }
  .back-text { font-size: 15px; }
  .front-text { font-size: 25px; }
</style>
</head>
<body>
<svg class="canvas" viewBox="0 0 1200 1147" xmlns="http://www.w3.org/2000/svg">
  <defs>
    <linearGradient id="band-edge" x1="0" x2="1" y1="0" y2="0">
      <stop offset="0" stop-color="var(--brown-deep)"/>
      <stop offset="0.12" stop-color="var(--gold-light)"/>
      <stop offset="0.88" stop-color="var(--gold-light)"/>
      <stop offset="1" stop-color="var(--brown-deep)"/>
    </linearGradient>
    <linearGradient id="paisley-fill" x1="0" x2="0" y1="0" y2="1">
      <stop offset="0" stop-color="var(--paisley-cream)"/>
      <stop offset="0.5" stop-color="var(--paisley-sage)"/>
      <stop offset="1" stop-color="var(--paisley-cream)"/>
    </linearGradient>
    <linearGradient id="band-fade" x1="0" x2="0" y1="0" y2="1">
      <stop offset="0" stop-color="var(--brown-mid)" stop-opacity="0"/>
      <stop offset="1" stop-color="var(--brown-deep)" stop-opacity="0.85"/>
    </linearGradient>
    <linearGradient id="banner-frame" x1="0" x2="1" y1="0" y2="0">
      <stop offset="0" stop-color="var(--brown-deep)"/>
      <stop offset="0.5" stop-color="var(--brown-mid)"/>
      <stop offset="1" stop-color="var(--brown-deep)"/>
    </linearGradient>
  </defs>

  <!-- Front label -->
  <g class="front-label">
    <rect class="front-band" x="220" y="0" width="190" height="500" fill="url(#band-edge)"/>
    <rect class="front-paisley-top" x="238" y="0" width="154" height="150" fill="url(#paisley-fill)" role="img" aria-label="Paisley pattern in cream and sage"/>
    <rect class="front-text-panel" x="238" y="150" width="154" height="140" fill="var(--label-white)"/>
    <rect class="front-paisley-bottom" x="238" y="380" width="154" height="120" fill="url(#paisley-fill)" role="img" aria-label="Paisley pattern in cream and sage"/>
    <rect class="front-band-fade" x="220" y="420" width="190" height="80" fill="url(#band-fade)"/>

    <text class="script-text front-text" x="315" y="186" text-anchor="middle">Marlowe Cloth</text>
    <text class="script-text front-text" x="315" y="216" text-anchor="middle">Handkerchief</text>
    <text class="script-text front-text" x="315" y="246" text-anchor="middle">by</text>

    <g class="banner-tails">
      <polygon points="96,322 170,322 170,392 96,392 126,357" fill="url(#banner-frame)"/>
      <polygon points="104,330 162,330 162,384 104,384 130,357" fill="var(--label-white)"/>
      <polygon points="470,322 550,322 520,357 550,392 470,392" fill="url(#banner-frame)"/>
      <polygon points="478,330 536,330 512,357 536,384 478,384" fill="var(--label-white)"/>
      <polygon points="150,380 170,392 170,380" fill="var(--brown-deep)"/>
      <polygon points="490,380 470,392 470,380" fill="var(--brown-deep)"/>
    </g>
    <rect class="banner-frame" x="150" y="290" width="340" height="90" fill="url(#banner-frame)"/>
    <rect class="banner-panel" x="160" y="300" width="320" height="70" fill="var(--label-white)"/>
    <text class="brand-name" x="320" y="348" text-anchor="middle" font-size="38">TENNICK</text>
  </g>

  <!-- Back label -->
  <g class="back-label">
    <polygon class="back-band" points="800,0 990,0 990,330 895,262 800,330" fill="url(#band-edge)"/>
    <rect class="back-paisley-top" x="818" y="0" width="154" height="62" fill="url(#paisley-fill)" role="img" aria-label="Paisley pattern in cream and sage"/>
    <rect class="back-text-panel" x="818" y="62" width="154" height="146" fill="var(--label-white)"/>
    <polygon class="back-paisley-bottom" points="818,208 972,208 972,310 895,256 818,310" fill="url(#paisley-fill)" role="img" aria-label="Paisley pattern in cream and sage"/>

    <text class="script-text back-text" x="895" y="100" text-anchor="middle">Made from imported</text>
    <text class="script-text back-text" x="895" y="122" text-anchor="middle">English Marlowe cloth</text>
    <text class="script-text back-text" x="895" y="144" text-anchor="middle">cotton %100</text>
    <text class="script-text back-text" x="895" y="166" text-anchor="middle">Traditional hemstitch finish</text>
    <text class="script-text back-text" x="895" y="188" text-anchor="middle">www.tennick-example.com</text>
  </g>
</svg>
</body>
</html>
```